Bright Arch Group business card

Bright Arch Group is the parent company of Bright Arch Building, Bright Arch Plumbing and Bright Arch Renovating. We require a sophisticated business card that covers all aspects of the building and plumbing space without using told or construction items.

Industry/Entity Type

Construction Company

Contact Information for Business Card

Gareth Pimley
Director
0472915083
gareth@brightarch.com.au
Www.brightarch.com.au

Font styles to use
Serif
Sans Serif

Colors
3176b5
ffce3e
0692cd
34a7d8
fbee3e
faa54b

Requirements
Must have
• Logo on front
• Logo and details on rear.
Nice to have
• Maybe water mark or shadow effect with logo
Should not have
• Tools or any construction associated items

```html
<!DOCTYPE html>
<html lang="en">
<head>
<meta charset="utf-8">
<title>Bright Arch Group Business Card</title>
<link rel="stylesheet" href="https://fonts.googleapis.com/css2?family=Open+Sans:wght@300;400;600&display=swap">
<style>
  :root {
    --bg: #e9e6e1;
    --card-dark: #0b0b0b;
    --card-light: #ffffff;
    --orange: #f58220;
    --ink: #111111;
    --shadow: rgba(0,0,0,0.25);
  }
  * { margin: 0; padding: 0; box-sizing: border-box; }
  html, body { width: 1200px; height: 900px; overflow: hidden; }
  body {
    background: var(--bg);
    font-family: "Open Sans", Arial, sans-serif;
    position: relative;
  }
  .card {
    position: absolute;
    left: 280px;
    width: 640px;
    height: 366px;
    box-shadow: 0 10px 24px var(--shadow);
    overflow: hidden;
  }
  .card--front { top: 54px; background: var(--card-dark); }
  .card--back { top: 480px; background: var(--card-light); }

  .brand {
    position: absolute;
    font-weight: 300;
    text-transform: uppercase;
    text-align: center;
    line-height: 1.15;
    white-space: nowrap;
  }
  .brand__line { display: block; }
  .brand__line--main { font-size: 40px; letter-spacing: 14px; }
  .brand__line--sub { font-size: 22px; letter-spacing: 18px; }
  .card--front .brand { color: var(--orange); left: 0; right: 0; top: 128px; }
  .card--back .brand { color: var(--ink); left: 250px; right: 0; top: 150px; }
  .card--back .brand__line--main { font-size: 32px; letter-spacing: 11px; }
  .card--back .brand__line--sub { font-size: 18px; letter-spacing: 15px; }

  .corner-mark { position: absolute; left: 0; top: 22px; }

  .person { position: absolute; left: 62px; top: 30px; }
  .person__name { color: var(--orange); font-weight: 600; font-size: 18px; line-height: 1.2; }
  .person__role { color: var(--ink); font-size: 12px; }

  .contact {
    position: absolute;
    left: 36px;
    top: 198px;
    list-style: none;
    color: var(--ink);
    font-size: 14px;
    line-height: 22px;
  }
  .contact__item { display: flex; align-items: center; gap: 9px; }
  .contact__icon { width: 11px; height: 11px; flex: none; }

  .footer-bands { position: absolute; left: 0; bottom: 0; }
</style>
</head>
<body>
  <section class="card card--front" aria-label="Card front">
    <div class="brand">
      <span class="brand__line brand__line--main">Bright Arch</span>
      <span class="brand__line brand__line--sub">Group</span>
    </div>
  </section>

  <section class="card card--back" aria-label="Card back">
    <svg class="corner-mark" width="50" height="40" viewBox="0 0 50 40" aria-hidden="true">
      <polygon points="0,0 16,0 6,14 0,14" fill="var(--orange)"/>
      <polygon points="20,6 46,6 46,38 0,38" fill="var(--ink)"/>
    </svg>

    <div class="person">
      <p class="person__name">Gareth Pimley</p>
      <p class="person__role">Director</p>
    </div>

    <div class="brand">
      <span class="brand__line brand__line--main">Bright Arch</span>
      <span class="brand__line brand__line--sub">Group</span>
    </div>

    <ul class="contact">
      <li class="contact__item">
        <svg class="contact__icon" viewBox="0 0 12 12" aria-hidden="true"><path d="M2 1l2 0 1 3-1.5 1a6 6 0 0 0 3.5 3.5L8 7l3 1v2a1 1 0 0 1-1 1A9 9 0 0 1 1 2a1 1 0 0 1 1-1z" fill="var(--orange)"/></svg>
        0472915083
      </li>
      <li class="contact__item">
        <svg class="contact__icon" viewBox="0 0 12 12" aria-hidden="true"><rect x="0.5" y="2.5" width="11" height="7" fill="var(--orange)"/><path d="M0.5 2.5l5.5 4 5.5-4" fill="none" stroke="#fff" stroke-width="1"/></svg>
        gareth@brightarch.com.au
      </li>
      <li class="contact__item">
        <svg class="contact__icon" viewBox="0 0 12 12" aria-hidden="true"><circle cx="6" cy="6" r="5.5" fill="var(--orange)"/><path d="M0.5 6h11M6 0.5c-3 3-3 8 0 11M6 0.5c3 3 3 8 0 11" fill="none" stroke="#fff" stroke-width="0.8"/></svg>
        Www.brightarch.com.au
      </li>
    </ul>

    <svg class="footer-bands" width="640" height="86" viewBox="0 0 640 86" aria-hidden="true">
      <polygon points="0,0 330,22 322,40 0,18" fill="var(--orange)"/>
      <polygon points="332,42 640,62 640,86 300,86" fill="var(--ink)"/>
    </svg>
  </section>
</body>
</html>
```